Visitenkarten-Design für Landschaftspfleger
Zielgruppe
Wir sind Landschaftspfleger kritischer Infrastruktur. Unsere Zielgruppe ist das operativer Management Großer Energiekonzerne die den Einkauf managen, Ausschreibungen und Vergabemaßnahmen organisieren.
Aufgabenstellung
Die Designs sollen nur die Logofarben enthalten, Weniger ist mehr.
Slogan:
Nachhaltige Netzpflege schützt NATURRÄUME!
Adresse: Amselweg 14
16837 Wildenhagen
Kilian Brauwer
M.Sc. Forstwirtschaft
Leiter Netz- / Anlagenpflege
Telefon:01769384712
mail: kilian.brauwer@lorvet.de
www.lorvet.de

```html
<!DOCTYPE html>
<html lang="de">
<head>
<meta charset="utf-8">
<title>Lorvet GmbH – Visitenkarte</title>
<link href="https://fonts.googleapis.com/css2?family=Lato:wght@400;700;900&display=swap" rel="stylesheet">
<style>
  :root {
    --brand-blue: #4b7d9d;
    --brand-green: #6aa84f;
    --brand-yellow: #e3c52b;
    --text-grey: #7a7a7a;
    --card-white: #f7f7f7;
    --page-bg: #ececec;
  }
  * { box-sizing: border-box; margin: 0; padding: 0; }
  html, body {
    width: 1200px; height: 954px; overflow: hidden;
    background: var(--page-bg);
    font-family: "Lato", sans-serif;
  }
  .sheet {
    width: 1200px; height: 954px;
    display: flex; flex-direction: column; align-items: center; justify-content: center;
    gap: 56px;
  }
  .card {
    position: relative;
    width: 580px; height: 375px;
    box-shadow: 0 6px 18px rgba(0,0,0,0.12);
    overflow: hidden;
  }
  /* Front */
  .card--front { background: var(--card-white); }
  .front-brand {
    position: absolute; left: 30px; top: 110px; width: 200px; height: 100px;
    border: 2px solid var(--brand-blue); border-radius: 20px;
    display: flex; align-items: center; justify-content: center; gap: 8px;
  }
  .brand-dot { width: 18px; height: 18px; border-radius: 50%; background: var(--brand-green); flex: none; }
  .brand-name { font-weight: 700; font-size: 24px; color: var(--brand-blue); white-space: nowrap; }
  .divider {
    position: absolute; left: 258px; top: 92px; width: 1px; height: 170px;
    background: #9a9a9a;
  }
  .contact { position: absolute; left: 280px; top: 96px; color: var(--text-grey); font-size: 14px; line-height: 1.35; white-space: nowrap; }
  .contact__name { font-weight: 700; font-size: 24px; color: var(--brand-blue); line-height: 1.1; margin-bottom: 4px; }
  .contact__address { margin-top: 8px; }
  .contact__list { list-style: none; margin-top: 8px; }
  .contact__list li { display: flex; align-items: center; gap: 8px; height: 20px; }
  .icon { width: 15px; height: 15px; flex: none; }
  .stripe { position: absolute; left: 0; bottom: 0; width: 580px; height: 8px; }
  /* Back */
  .card--back { background: var(--brand-blue); color: #fff; }
  .back-brand {
    position: absolute; left: 50%; top: 110px; transform: translateX(-50%);
    width: 230px; height: 110px; border: 2px solid #fff; border-radius: 22px;
    display: flex; align-items: center; justify-content: center; gap: 10px;
  }
  .back-brand .brand-dot { background: #fff; width: 22px; height: 22px; }
  .back-brand .brand-name { color: #fff; font-size: 28px; }
  .slogan {
    position: absolute; left: 0; right: 0; top: 250px; text-align: center;
    font-size: 17px; letter-spacing: 0.4px;
  }
  .slogan strong { font-weight: 900; }
</style>
</head>
<body>
<main class="sheet">
  <section class="card card--front" aria-label="Vorderseite">
    <div class="front-brand">
      <span class="brand-dot"></span>
      <span class="brand-name">Lorvet GmbH</span>
    </div>
    <div class="divider"></div>
    <div class="contact">
      <p class="contact__name">Kilian Brauwer</p>
      <p>M.Sc. Forstwirtschaft</p>
      <p>Leiter Netz- / Anlagenpflege</p>
      <p class="contact__address">Amselweg 14<br>16837 Wildenhagen</p>
      <ul class="contact__list">
        <li>
          <svg class="icon" viewBox="0 0 16 16"><rect width="16" height="16" rx="3" fill="var(--brand-blue)"/><path d="M5 3.5h2l.8 2.5-1.3 1a6 6 0 0 0 2.5 2.5l1-1.3 2.5.8v2a1 1 0 0 1-1 1A8.5 8.5 0 0 1 4 4.5a1 1 0 0 1 1-1z" fill="#fff"/></svg>
          <span>01769384712</span>
        </li>
        <li>
          <svg class="icon" viewBox="0 0 16 16"><rect width="16" height="16" rx="3" fill="var(--brand-blue)"/><rect x="3" y="4.5" width="10" height="7" fill="none" stroke="#fff" stroke-width="1.2"/><path d="M3 4.5l5 4 5-4" fill="none" stroke="#fff" stroke-width="1.2"/></svg>
          <span>kilian.brauwer@lorvet.de</span>
        </li>
        <li>
          <svg class="icon" viewBox="0 0 16 16"><rect width="16" height="16" rx="3" fill="var(--brand-blue)"/><circle cx="8" cy="8" r="4.5" fill="none" stroke="#fff" stroke-width="1.1"/><ellipse cx="8" cy="8" rx="2" ry="4.5" fill="none" stroke="#fff" stroke-width="1"/><path d="M3.5 8h9" stroke="#fff" stroke-width="1"/></svg>
          <span>www.lorvet.de</span>
        </li>
      </ul>
    </div>
    <svg class="stripe" viewBox="0 0 580 8" preserveAspectRatio="none">
      <polygon points="0,0 196,0 200,8 0,8" fill="var(--brand-yellow)"/>
      <polygon points="198,0 392,0 396,8 202,8" fill="var(--brand-green)"/>
      <polygon points="396,0 580,0 580,8 400,8" fill="var(--brand-blue)"/>
    </svg>
  </section>

  <section class="card card--back" aria-label="Rückseite">
    <div class="back-brand">
      <span class="brand-dot"></span>
      <span class="brand-name">Lorvet GmbH</span>
    </div>
    <p class="slogan">Nachhaltige Netzpflege schützt <strong>NATURRÄUME!</strong></p>
  </section>
</main>
</body>
</html>
```